Signs to Go on the Side of Shipping Containers

We are a startup in North Alabama that will lease/sale shipping containers as Portable Storage options for business/construction sites. We need signs that will be mass produced and be mounted on every side of the container for advertising/visibility.
We need multiple sizes depending on the side the sign will be on/ the size of the container it is being mounted on.
Website: www.ridgelinebinworks.com

MUST BE SIMPLE AND EASY TO READ. Not to Busy. See example in
Updates

One designer is asking me to extend deadline. This is my first design project so not sure why they want me to do this but figured I would.

Target Market(s)

Business owners/Construction Companies/Individuals Moving

Industry/Entity Type

Portable Storage

Colors
0054AA
0677BA
7BADD7
CADEEF
E8F1F8

Requirements
Must have
• Company Name(Ridgeline Bin Works)/Phone Number (256-555-0147)/Website (www.ridgelinebinworks.com
Nice to have
• Play on the container shapes/pattern.

```html
<!DOCTYPE html>
<html lang="en">
<head>
<meta charset="utf-8">
<title>Ridgeline Bin Works – Container Sign</title>
<link rel="stylesheet" href="https://fonts.googleapis.com/css2?family=Anton&family=Montserrat:wght@700;800&display=swap">
<style>
  :root {
    --stage: #231f20;
    --blue-deep: #0054aa;
    --blue-brand: #0677ba;
    --blue-mid: #3a7cc4;
    --blue-soft: #7badd7;
    --blue-pale: #cadeef;
    --blue-mist: #dae8f5;
    --ink: #050505;
    --white: #ffffff;
  }
  * { margin: 0; padding: 0; box-sizing: border-box; }
  html, body { width: 1200px; height: 1200px; overflow: hidden; background: var(--stage); }
  .sign {
    position: absolute; left: 37px; top: 319px; width: 1126px; height: 563px;
    background:
      repeating-linear-gradient(90deg,
        #3272bd 0 10px, #3c86cf 10px 14px, #2f6cb6 14px 24px, #3a80c9 24px 28px);
    overflow: hidden;
  }
  .header-panel {
    position: absolute; left: 51px; top: 0; width: 1025px; height: 298px;
    background: var(--blue-mist);
    border-radius: 0 0 58px 58px;
  }
  .container-photo {
    position: absolute; left: 42px; top: 31px; width: 267px; height: 244px;
    background: linear-gradient(160deg, #2b7fb0 0%, #16628f 60%, #0d4f78 100%);
    clip-path: polygon(0 20%, 76% 0, 100% 34%, 100% 80%, 76% 100%, 0 84%);
  }
  .brand {
    position: absolute; left: 300px; top: 30px; width: 690px;
    text-align: center; font-family: "Anton", sans-serif; font-weight: 400;
    color: var(--blue-brand); line-height: 1;
  }
  .brand-line-top { display: block; font-size: 74px; letter-spacing: 2px; }
  .brand-line-main { display: block; font-size: 112px; letter-spacing: 1px; margin-top: -4px; }
  .tagline {
    position: absolute; left: 300px; top: 236px; width: 690px; text-align: center;
    font-family: "Montserrat", sans-serif; font-weight: 800; font-size: 36px;
    letter-spacing: 12px; color: var(--ink); line-height: 1;
  }
  .phone-row {
    position: absolute; left: 0; top: 328px; width: 1126px;
    display: flex; justify-content: center; align-items: center; gap: 18px;
  }
  .phone-icon { width: 68px; height: 84px; }
  .phone-number {
    font-family: "Montserrat", sans-serif; font-weight: 700; font-size: 118px;
    color: var(--white); line-height: 1; letter-spacing: 1px;
    text-shadow: 2px 3px 4px rgba(0, 30, 80, 0.45);
  }
  .web-pill {
    position: absolute; left: 36px; top: 452px; width: 1044px; height: 86px;
    border-radius: 43px; border: 3px solid var(--white);
    background: linear-gradient(180deg, var(--blue-mist) 0%, var(--blue-pale) 50%, var(--blue-soft) 100%);
    display: flex; justify-content: center; align-items: center;
    font-family: "Montserrat", sans-serif; font-weight: 800; font-size: 54px;
    color: var(--ink); letter-spacing: 1px;
  }
  .web-pill .domain { color: #2f66b3; }
</style>
</head>
<body>
  <section class="sign">
    <div class="header-panel">
      <div class="container-photo" role="img" aria-label="Blue shipping container photo"></div>
      <h1 class="brand">
        <span class="brand-line-top">RIDGELINE</span>
        <span class="brand-line-main">BIN WORKS</span>
      </h1>
      <p class="tagline">SALES &amp; RENTALS</p>
    </div>

    <div class="phone-row">
      <svg class="phone-icon" viewBox="0 0 68 84" aria-hidden="true">
        <path d="M14 6 C6 8 2 16 4 30 C8 52 20 70 34 80 C40 84 46 82 50 76 L44 62 C42 58 38 58 34 62 C26 54 20 42 18 30 C22 28 24 24 22 20 Z"
              fill="#d6ecfb" stroke="#5a9ad6" stroke-width="2"/>
        <path d="M34 24 A12 12 0 0 1 42 40" fill="none" stroke="#d6ecfb" stroke-width="5" stroke-linecap="round"/>
        <path d="M38 14 A22 22 0 0 1 52 44" fill="none" stroke="#d6ecfb" stroke-width="5" stroke-linecap="round"/>
        <path d="M42 4 A32 32 0 0 1 63 48" fill="none" stroke="#d6ecfb" stroke-width="5" stroke-linecap="round"/>
      </svg>
      <span class="phone-number">256-555-0147</span>
    </div>

    <div class="web-pill">www.<span class="domain">ridgelinebinworks</span>.com</div>
  </section>
</body>
</html>
```